P.L.U.S.O.N. Content Framework Infographic

I am looking to take my basic infographic to the next level. I need to to translate the content marketing concept that is outlined in the uploaded file. I have attached the content and the image I would like used. I am not stuck on the colors represented in the image but do want to see a variety of options.

Target Market(s)

Companies that are looking for a content marketing strategy, SEO Agencies, marketing agencies

Industry/Entity Type

Digital marketing, SEO

Font styles to use
Other font styles liked:
• arial, calibri are fine

Colors
0054AA
0677BA
7BADD7
CADEEF
E8F1F8
0094D4
00A9DD
6FCCEA
C7EBF8
E9F6FB
00AB8E
00BBA5
67D7C9
C6EFE9
E9F9F6
59FF00
82FF00
B8FF75
E3FFCB
F4FFEA
EE7325
F08F49
F5BC92
FAE3D3
FDF4ED
EB3D1F
EC4F4E
F09395
F8D3D4
FCEDEE

Requirements
Must have
• The image that I provided with the content breakdown with section connectors to the image
Nice to have
• a few different way to present the data

```html
<!DOCTYPE html>
<html lang="en">
<head>
<meta charset="utf-8">
<title>Putting P.L.U.S.O.N. On The Bone</title>
<link rel="stylesheet" href="https://fonts.googleapis.com/css2?family=Montserrat:wght@700;800;900&family=Open+Sans:wght@400;600;700&display=swap">
<style>
  :root{
    --navy:#1c2a6b;
    --purple:#4b2a8f;
    --blue-deep:#0054AA;
    --blue:#0677BA;
    --blue-light:#7BADD7;
    --sky:#00A9DD;
    --paper:#f4f5fa;
    --white:#ffffff;
    --ink:#2b2f3a;
    --green:#00AB8E;
    --lime:#6cc24a;
    --red:#EB3D1F;
    --pink:#e5427a;
    --orange:#EE7325;
    --yellow:#f6c944;
  }
  *{box-sizing:border-box;margin:0;padding:0}
  html,body{width:849px;height:1200px;overflow:hidden;background:var(--paper)}
  .poster{position:relative;width:849px;height:1200px;overflow:hidden;
    background:linear-gradient(180deg,#eef0f8 0%,#f8f9fc 60%,#eef3f8 100%);
    font-family:"Open Sans",Arial,sans-serif;color:var(--ink)}
  .edge-strip{position:absolute;left:0;top:0;width:22px;height:100%;
    background:linear-gradient(180deg,var(--purple),var(--blue) 55%,var(--sky))}
  .top-band{position:absolute;left:0;top:0;width:100%;height:70px;
    background:linear-gradient(90deg,var(--purple),var(--blue-deep) 60%,var(--sky))}
  .title-banner{position:absolute;left:44px;top:34px;width:760px;height:142px;background:var(--white);
    border-radius:10px;box-shadow:0 6px 18px rgba(28,42,107,.18);display:flex;align-items:center}
  .title-block{flex:1;text-align:center;padding-left:40px}
  .title{font-family:"Montserrat",Arial,sans-serif;font-weight:900;font-size:50px;color:var(--navy);letter-spacing:1px;line-height:1.05}
  .subtitle{font-family:"Montserrat",Arial,sans-serif;font-weight:700;font-size:21px;color:var(--blue);margin-top:8px}
  .tag{width:130px;height:142px;background:var(--blue-deep);color:var(--white);border-radius:0 10px 10px 0;
    display:flex;align-items:center;justify-content:center;text-align:center;
    font-family:"Montserrat",Arial,sans-serif;font-weight:800;font-size:18px;line-height:1.25}
  .intro{position:absolute;left:54px;top:196px;width:740px;font-size:12.2px;line-height:1.5;color:var(--ink)}
  .intro strong{color:var(--blue-deep)}
  .card{position:absolute;width:360px;height:245px}
  .card-head{position:absolute;left:0;top:0;width:100%;height:50px;border-radius:8px;color:var(--white);
    display:flex;align-items:center;justify-content:space-between;padding:0 10px 0 18px;
    font-family:"Montserrat",Arial,sans-serif;font-weight:800;font-size:19px;letter-spacing:.5px;
    box-shadow:0 4px 10px rgba(0,0,0,.15);z-index:2}
  .card-num{width:36px;height:36px;border-radius:50%;background:var(--white);display:flex;align-items:center;justify-content:center;font-size:19px}
  .card-body{position:absolute;left:10px;top:40px;right:10px;bottom:0;background:var(--white);border:2px solid;border-radius:0 0 10px 10px;
    padding:20px 16px 12px;font-size:11.6px;line-height:1.5}
  .c1{left:50px;top:350px}.c2{left:440px;top:350px}
  .c3{left:50px;top:615px}.c4{left:440px;top:615px}
  .c5{left:50px;top:880px}.c6{left:440px;top:880px}
  .green .card-head{background:var(--green)}.green .card-num{color:var(--green)}.green .card-body{border-color:var(--green)}
  .red .card-head{background:var(--red)}.red .card-num{color:var(--red)}.red .card-body{border-color:var(--red)}
  .orange .card-head{background:var(--orange)}.orange .card-num{color:var(--orange)}.orange .card-body{border-color:var(--orange)}
  .lime .card-head{background:var(--lime)}.lime .card-num{color:var(--lime)}.lime .card-body{border-color:var(--lime)}
  .blue .card-head{background:var(--blue-deep)}.blue .card-num{color:var(--blue-deep)}.blue .card-body{border-color:var(--blue-deep)}
  .pink .card-head{background:var(--pink)}.pink .card-num{color:var(--pink)}.pink .card-body{border-color:var(--pink)}
  .base-stripes{position:absolute;left:0;bottom:0;width:100%;height:60px}
</style>
</head>
<body>
<div class="poster">
  <div class="top-band"></div>
  <div class="edge-strip"></div>

  <header class="title-banner">
    <div class="title-block">
      <h1 class="title">PUTTING P.L.U.S.O.N.</h1>
      <p class="subtitle">On The Bone For The User &amp; Searchly To Chew On</p>
    </div>
    <div class="tag">INFO<br>GRAPICH</div>
  </header>

  <p class="intro"><strong>In SEO content is still king.</strong> What has changed with content is not the content but the delivery of that content. People these days are consuming content in so many different places &amp; formats that it makes it difficult to create engaging content that ranks and converts. Some people prefer to continue reading webpages to find the information they are looking for. Some prefer to see the pictures because they are more visual than contextual. Others would prefer to just watch video on Vidstream or other online video platforms, and in some cases it is more of an auditory way such as podcast &amp; streaming radio platforms. This infographic will breakdown how all of the pieces fit together to get "P.L.U.S.O.N." on the bone.</p>

  <section class="card c1 green">
    <div class="card-head">MULTIMEDIA<span class="card-num">1</span></div>
    <div class="card-body">"Multimedia" consists of infographics, specific images, embedded videos, and other types of content aside from the written word. By doing this you provide the same content to audiences that differ based on how they choose to consume content. Online content marketing with multimedia is highly engaging as it presents needed information in a multifaceted but direct and timely manner.</div>
  </section>

  <section class="card c2 red">
    <div class="card-head">ENGAGEMENT<span class="card-num">2</span></div>
    <div class="card-body">"Engagement" is essential for views and conversion as it keeps readers locked in on content to the point that they are more likely to move through the website experience and considers the value offered in the minutes, hours, days, and weeks that follow their website visit.</div>
  </section>

  <section class="card c3 orange">
    <div class="card-head">EXPERTISE<span class="card-num">3</span></div>
    <div class="card-body">"Expertise" refers to the content writer's level of knowledge or skill in a specific subject area that is relevant to the user's search query. High quality content should be created by someone with relevant expertise in the topic being discussed.</div>
  </section>

  <section class="card c4 lime">
    <div class="card-head">EXPERIENCE<span class="card-num">4</span></div>
    <div class="card-body">"Experience" in short means that Searchly values firsthand or life experience of the author on the topic a page is about. It is important because often searchers want to know first hand information before they decide to purchase something or use a certain service.</div>
  </section>

  <section class="card c5 blue">
    <div class="card-head">AUTHORITATIVENESS<span class="card-num">5</span></div>
    <div class="card-body">"Authoritativeness" refers to the credibility of the content and the website it is hosted on. Authoritativeness can be established through the quality of the content, the site's reputation, author's reputation, external links &amp; content citations, and the credentials of the content creator.</div>
  </section>

  <section class="card c6 pink">
    <div class="card-head">TRUSTWORTHINESS<span class="card-num">6</span></div>
    <div class="card-body">"Trustworthiness" is the final result of doing all of the above. If you write content that is helpful, knowledgeable, first hand based on experience from someone who is an expert in their field, you get the trust of users consuming your content. If you can gain the user's trust about your content, Searchly and other search engines will trust you and will provide you with the organic visibility we all strive for.</div>
  </section>

  <svg class="base-stripes" viewBox="0 0 849 60" preserveAspectRatio="none" aria-hidden="true">
    <path d="M0 40 L849 14 L849 24 L0 50 Z" fill="var(--yellow)"/>
    <path d="M0 52 L849 28 L849 40 L0 60 Z" fill="var(--sky)"/>
    <path d="M0 60 L849 44 L849 60 Z" fill="var(--purple)"/>
  </svg>
</div>
</body>
</html>
```